Bramblecrest Roofing Co. business card design

I am a Roofing contractor in Texas. The name of my company is Bramblecrest Roofing Co. I also offer a few other services (Christmas light installation, gutters, fencing, pressure washing). However my main gig is roofing. Storm restoration and knowledge of the insurance claim process is my specialty.

My colors are black, red and white. I’d like something pretty simple and clean. Modern looking but with a splash of this red tartan pattern.

I have another version of my logo being edited at the moment where the little top part of the F in roofing that’s currently tartan will be changed to just solid red to make it more visible. So if that’s something you can change in your mock up great. But I can provide the full version once the contest is complete

Target Market(s)

Homeowners

Industry/Entity Type

Roofing

Contact Information for Business Card

Darren Pike. 682-555-0193. www.bramblecrest roofing.example Darren@bramblecrestroofing.example

Colors
EB3D1F
EC4F4E
F09395
F8D3D4
FCEDEE

Requirements
Nice to have
• Maybe instead of a business address. I could say serving all DFW Texas or something like that. And maybe add a line somewhere saying deductible assistance? Just a thought

```html
<!DOCTYPE html>
<html lang="en">
<head>
<meta charset="utf-8">
<title>Bramblecrest Roofing Co. – Business Card</title>
<link href="https://fonts.googleapis.com/css2?family=Montserrat:wght@400;500;700;800&display=swap" rel="stylesheet">
<style>
  :root {
    --red: #d71f26;
    --red-dark: #8e1519;
    --black: #141414;
    --ink: #2a2a2a;
    --white: #ffffff;
    --backdrop: #d9d9d7;
  }
  * { box-sizing: border-box; margin: 0; padding: 0; }
  html, body {
    width: 1200px; height: 801px; overflow: hidden;
    background: var(--backdrop);
    font-family: "Montserrat", Arial, sans-serif;
  }
  .stage {
    width: 1200px; height: 801px;
    display: flex; align-items: center; justify-content: center; gap: 40px;
  }
  .card {
    position: relative;
    width: 540px; height: 309px;
    background: var(--white);
    border-radius: 18px;
    border-bottom: 3px solid var(--red);
    box-shadow: 0 10px 28px rgba(0,0,0,.18);
    overflow: hidden;
  }

  /* Front side */
  .wordmark {
    color: var(--red);
    font-weight: 800;
    text-transform: uppercase;
    line-height: 1;
    letter-spacing: .5px;
  }
  .card-front .wordmark {
    position: absolute; left: 34px; top: 36px;
    font-size: 27px;
  }
  .card-front .wordmark span { display: block; font-size: 21px; margin-top: 4px; }
  .card-front .logo-disc {
    position: absolute; right: 40px; top: 30px;
    width: 170px; height: 170px; border-radius: 50%;
    background: radial-gradient(circle at 40% 40%, var(--red) 0%, var(--red) 55%, var(--red-dark) 100%);
  }
  .accent-block {
    position: absolute; left: 0; top: 132px;
    width: 24px; height: 40px;
    background: var(--red);
  }
  .person { position: absolute; left: 40px; top: 128px; }
  .person-name {
    color: var(--red); font-weight: 700; font-size: 17px;
    text-transform: uppercase; letter-spacing: .5px;
  }
  .person-title { color: var(--ink); font-size: 12px; font-weight: 500; margin-top: 3px; }
  .address { color: var(--ink); font-size: 12px; line-height: 1.45; margin-top: 14px; }
  .contacts { list-style: none; margin-top: 12px; }
  .contacts li {
    display: flex; align-items: center; gap: 8px;
    color: var(--ink); font-size: 12px; line-height: 1.7;
  }
  .contacts svg { width: 12px; height: 12px; fill: var(--red); flex: none; }

  /* Back side */
  .card-back {
    display: flex; flex-direction: column; align-items: center; justify-content: center;
    gap: 22px;
  }
  .card-back .logo-disc {
    width: 130px; height: 130px; border-radius: 50%;
    background: radial-gradient(circle at 40% 40%, var(--red) 0%, var(--red) 55%, var(--red-dark) 100%);
  }
  .card-back .wordmark { font-size: 30px; text-align: center; }
  .card-back .wordmark span { display: block; font-size: 22px; margin-top: 5px; }
</style>
</head>
<body>
<main class="stage">
  <section class="card card-front">
    <div class="wordmark">Bramblecrest<span>Roofing Co.</span></div>
    <div class="logo-disc" role="img" aria-label="Company emblem area in red tones"></div>
    <div class="accent-block"></div>
    <div class="person">
      <p class="person-name">Darren Pike</p>
      <p class="person-title">Managing Director</p>
      <p class="address">Your address, City<br>State, Zip 1234</p>
      <ul class="contacts">
        <li><svg viewBox="0 0 24 24"><path d="M6.6 10.8a15.1 15.1 0 0 0 6.6 6.6l2.2-2.2a1 1 0 0 1 1-.25 11.4 11.4 0 0 0 3.6.57 1 1 0 0 1 1 1V20a1 1 0 0 1-1 1A17 17 0 0 1 3 4a1 1 0 0 1 1-1h3.5a1 1 0 0 1 1 1c0 1.25.2 2.45.57 3.57a1 1 0 0 1-.25 1z"/></svg>682-555-0193</li>
        <li><svg viewBox="0 0 24 24"><path d="M2 5h20v14H2zm2 2v.5l8 5 8-5V7l-8 5z"/></svg>Darren@bramblecrestroofing.example</li>
        <li><svg viewBox="0 0 24 24"><path d="M12 2a10 10 0 1 0 0 20 10 10 0 0 0 0-20zm6.9 6h-3a15.6 15.6 0 0 0-1.3-3.9A8 8 0 0 1 18.9 8zM12 4c.8 1.2 1.5 2.5 1.9 4h-3.8c.4-1.5 1.1-2.8 1.9-4zM4.3 14a8.2 8.2 0 0 1 0-4h3.4a16.5 16.5 0 0 0 0 4zm.8 2h3a15.6 15.6 0 0 0 1.3 3.9A8 8 0 0 1 5.1 16zm3-8h-3a8 8 0 0 1 4.3-3.9C8.8 5.3 8.4 6.6 8.1 8zM12 20c-.8-1.2-1.5-2.5-1.9-4h3.8c-.4 1.5-1.1 2.8-1.9 4zm2.3-6H9.7a14.7 14.7 0 0 1 0-4h4.6a14.7 14.7 0 0 1 0 4zm.3 5.9c.6-1.2 1-2.5 1.3-3.9h3a8 8 0 0 1-4.3 3.9zm1.7-5.9a16.5 16.5 0 0 0 0-4h3.4a8.2 8.2 0 0 1 0 4z"/></svg>www.bramblecrestroofing.example</li>
      </ul>
    </div>
  </section>

  <section class="card card-back">
    <div class="logo-disc" role="img" aria-label="Company emblem area in red tones"></div>
    <div class="wordmark">Bramblecrest<span>Roofing Co.</span></div>
  </section>
</main>
</body>
</html>
```